Gelato Business Card

create a new business card using existing logo

Target Market(s)

B2B

Contact Information for Business Card

typical contact info: logo, address, email, phone, rep name

Colors
0355a3
33a6d7

Requirements
Must have
• a feel of high quality, luxury, happiness
• use cool, comforting color and texture of business card.
Nice to have
• "A Little Perfection Goes A Long Way!" TM
• or, "more quality, more flavor"
• or, "Flavor Matters"

```html
<!DOCTYPE html>
<html lang="en">
<head>
<meta charset="utf-8">
<title>Bellamare Business Card</title>
<link rel="stylesheet" href="https://fonts.googleapis.com/css2?family=Cinzel:wght@600&family=Cormorant+Garamond:wght@500;700&display=swap">
<style>
  :root {
    --backdrop: #2fb3a2;
    --card-white: #ffffff;
    --navy: #3a3f98;
    --sky: #4a9dcb;
    --gold: #f2a63a;
    --red: #e3263b;
    --ink-light: #ffffff;
  }
  * { margin: 0; padding: 0; box-sizing: border-box; }
  html, body {
    width: 1200px; height: 895px; overflow: hidden;
    background: var(--backdrop);
  }
  .canvas {
    width: 1200px; height: 895px;
    display: flex; flex-direction: column;
    align-items: center; justify-content: center; gap: 40px;
  }
  .card {
    position: relative;
    width: 680px; height: 388px;
    background: var(--card-white);
    box-shadow: 0 8px 22px rgba(0,0,0,0.25);
    overflow: hidden;
    font-family: "Cormorant Garamond", Georgia, serif;
  }
  /* Front */
  .brand-lockup {
    position: absolute; left: 0; right: 0; top: 140px;
    display: flex; align-items: center; justify-content: center; gap: 16px;
  }
  .brand-dot {
    width: 22px; height: 22px; border-radius: 50%;
    background: var(--sky);
  }
  .brand-name {
    font-family: "Cormorant Garamond", Georgia, serif;
    font-weight: 700; font-size: 78px; line-height: 1;
    color: var(--navy); letter-spacing: 1px;
  }
  .front .web {
    position: absolute; right: 58px; bottom: 42px;
    font-size: 20px; font-weight: 500; color: var(--navy); letter-spacing: 0.5px;
  }
  .front .web .domain { color: var(--gold); }
  /* Back */
  .back { background: var(--sky); }
  .back .swoosh { position: absolute; inset: 0; }
  .back .brand-lockup { top: auto; bottom: 118px; right: auto; left: 40px; gap: 10px; }
  .back .brand-name { font-size: 50px; }
  .back .brand-dot { width: 15px; height: 15px; }
  .contact {
    position: absolute; right: 38px; top: 36px;
    text-align: right; color: var(--ink-light);
  }
  .rep-name {
    font-family: "Cinzel", Georgia, serif; font-weight: 600;
    font-size: 26px; color: var(--gold); letter-spacing: 1px;
  }
  .rep-title { font-size: 19px; font-weight: 500; margin-top: 2px; }
  .address { font-size: 18px; font-weight: 500; line-height: 1.35; margin-top: 30px; }
  .channels { list-style: none; margin-top: 30px; font-size: 18px; font-weight: 500; line-height: 1.55; }
  .channels li { display: flex; align-items: center; justify-content: flex-end; gap: 10px; }
  .channels svg { width: 15px; height: 15px; fill: var(--gold); flex: none; }
</style>
</head>
<body>
<main class="canvas">
  <section class="card front">
    <div class="brand-lockup">
      <span class="brand-dot"></span>
      <span class="brand-name">Bellamare</span>
    </div>
    <p class="web">www.<span class="domain">bellamare</span>.com</p>
  </section>

  <section class="card back">
    <svg class="swoosh" viewBox="0 0 680 388" aria-hidden="true">
      <circle cx="80" cy="330" r="344" fill="var(--red)"/>
      <circle cx="80" cy="330" r="340" fill="var(--navy)"/>
      <circle cx="70" cy="345" r="318" fill="var(--card-white)"/>
    </svg>
    <div class="brand-lockup">
      <span class="brand-dot"></span>
      <span class="brand-name">Bellamare</span>
    </div>
    <div class="contact">
      <h1 class="rep-name">MARCUS ELLERY</h1>
      <p class="rep-title">Founder &amp; CEO</p>
      <p class="address">48 Harbour Lane, Suite B<br>Bristol, UK BS1 4QT</p>
      <ul class="channels">
        <li>020 7946 0321
          <svg viewBox="0 0 24 24"><path d="M6.6 10.8a15 15 0 0 0 6.6 6.6l2.2-2.2a1 1 0 0 1 1-.25 11.4 11.4 0 0 0 3.6.57 1 1 0 0 1 1 1V20a1 1 0 0 1-1 1A17 17 0 0 1 3 4a1 1 0 0 1 1-1h3.5a1 1 0 0 1 1 1c0 1.25.2 2.45.57 3.6a1 1 0 0 1-.25 1z"/></svg>
        </li>
        <li>m_ellery@bellamare.com
          <svg viewBox="0 0 24 24"><path d="M2 5h20v14H2z M2 5l10 8 10-8" stroke="var(--sky)" stroke-width="1.5"/></svg>
        </li>
        <li>www.bellamare.com
          <svg viewBox="0 0 24 24"><circle cx="12" cy="12" r="10"/><path d="M2 12h20M12 2c3 3 3 17 0 20M12 2c-3 3-3 17 0 20" stroke="var(--sky)" stroke-width="1.4" fill="none"/></svg>
        </li>
      </ul>
    </div>
  </section>
</main>
</body>
</html>
```